Coralbend Pastoral Traders Business Cards

We require business cards revamped with our logo. A few details we would like to use.

1. Round Edges
2. Our logo over the top of a wagyu cattle background photo on one side of the card

Other side of the card has the below details.

1. Person Name (First & Last)
2. Job Position
3. Mobile Number
4. Email Address
5. Website Address

Simple & Neat.

Target Market(s)

Sales

Industry/Entity Type

Agriculture

Contact Information for Business Card

CORALBEND PASTORAL TRADERS

Colors

Designer to choose colors to be used in the design.

Requirements
Must have
• Company Logo

```html
<!DOCTYPE html>
<html lang="en">
<head>
<meta charset="utf-8">
<title>Coralbend Pastoral Traders – Business Cards</title>
<link rel="stylesheet" href="https://fonts.googleapis.com/css2?family=Open+Sans:wght@400;700&display=swap">
<style>
  :root {
    --page-bg: #ffffff;
    --card-dark: #140809;
    --maroon: #6a1620;
    --maroon-logo: #7c1d28;
    --ink: #1a0a0b;
    --photo-light: #4a4446;
    --photo-mid: #262022;
    --photo-deep: #120a0b;
    --logo-light: #e9e1e2;
  }
  * { box-sizing: border-box; margin: 0; padding: 0; }
  html, body {
    width: 1200px; height: 860px; overflow: hidden;
    background: var(--page-bg);
    font-family: "Open Sans", Arial, sans-serif;
  }
  .sheet { position: relative; width: 1200px; height: 860px; }
  .card {
    position: absolute; top: 286px;
    width: 444px; height: 287px;
    border-radius: 37px; overflow: hidden;
  }
  .card--front { left: 131px; background: var(--card-dark); }
  .card--back { left: 625px; background: var(--card-dark); }

  .cattle-photo {
    position: absolute; inset: 0;
    background:
      radial-gradient(ellipse 55% 45% at 42% 52%, var(--photo-light) 0%, var(--photo-mid) 55%, transparent 80%),
      radial-gradient(ellipse 30% 40% at 88% 25%, var(--photo-mid) 0%, transparent 75%),
      linear-gradient(180deg, var(--photo-deep) 0%, var(--photo-deep) 12%, #1c1517 40%, #1a1315 100%);
  }
  .front-brand {
    position: absolute; left: 0; right: 30px; top: 112px;
    text-align: center; color: var(--logo-light);
    font-weight: 700; line-height: 1.1;
  }
  .front-brand .brand-main { font-size: 31px; letter-spacing: 1px; display: block; }
  .front-brand .brand-sub { font-size: 14px; letter-spacing: 4px; display: block; margin-top: 4px; }

  .back-wave { position: absolute; inset: 0; }
  .back-brand {
    position: absolute; left: 0; right: 0; top: 48px;
    text-align: center; color: var(--maroon-logo);
    font-weight: 700; line-height: 1.1;
  }
  .back-brand .brand-main { font-size: 27px; letter-spacing: 1px; display: block; }
  .back-brand .brand-sub { font-size: 12px; letter-spacing: 4px; display: block; margin-top: 3px; }

  .holder { position: absolute; left: 29px; top: 194px; color: var(--ink); }
  .holder-name { font-size: 17px; font-weight: 700; letter-spacing: .3px; }
  .holder-role { font-size: 14px; font-weight: 400; margin-top: 1px; }

  .contact-list {
    position: absolute; left: 219px; top: 190px;
    list-style: none; color: var(--ink); font-size: 12.5px; line-height: 17px;
  }
  .contact-list li { display: flex; align-items: center; gap: 4px; }
  .contact-icon { width: 10px; height: 10px; flex: none; }
</style>
</head>
<body>
<main class="sheet">
  <section class="card card--front" aria-label="Card front">
    <div class="cattle-photo" role="img" aria-label="Photograph of a black wagyu bull standing side-on against a dark background"></div>
    <div class="front-brand">
      <span class="brand-main">CORALBEND</span>
      <span class="brand-sub">PASTORAL TRADERS</span>
    </div>
  </section>

  <section class="card card--back" aria-label="Card back">
    <svg class="back-wave" viewBox="0 0 444 287" preserveAspectRatio="none" aria-hidden="true">
      <path d="M0 105 C 40 92, 80 96, 140 108 S 260 150, 330 146 S 420 125, 444 114 L444 287 L0 287 Z" fill="var(--maroon)"/>
      <path d="M0 140 C 40 122, 90 122, 160 136 S 280 168, 340 160 S 420 140, 444 122 L444 128 C 420 146, 380 166, 330 168 S 200 148, 150 138 S 40 130, 0 146 Z" fill="var(--card-dark)"/>
    </svg>
    <div class="back-brand">
      <span class="brand-main">CORALBEND</span>
      <span class="brand-sub">PASTORAL TRADERS</span>
    </div>
    <div class="holder">
      <p class="holder-name">PERSON NAME</p>
      <p class="holder-role">Job Position</p>
    </div>
    <ul class="contact-list">
      <li>
        <svg class="contact-icon" viewBox="0 0 10 10" aria-hidden="true"><circle cx="5" cy="5" r="5" fill="var(--ink)"/><rect x="3.2" y="2" width="3.6" height="6" rx=".6" fill="var(--maroon)"/></svg>
        +00 123 456 789
      </li>
      <li>
        <svg class="contact-icon" viewBox="0 0 10 10" aria-hidden="true"><circle cx="5" cy="5" r="5" fill="var(--ink)"/><rect x="2.3" y="3" width="5.4" height="4" fill="var(--maroon)"/><path d="M2.3 3 L5 5.3 L7.7 3" stroke="var(--ink)" stroke-width=".6" fill="none"/></svg>
        person@coralbendpastoral.com
      </li>
      <li>
        <svg class="contact-icon" viewBox="0 0 10 10" aria-hidden="true"><circle cx="5" cy="5" r="5" fill="var(--ink)"/><circle cx="5" cy="5" r="3" fill="none" stroke="var(--maroon)" stroke-width=".7"/><path d="M2 5 H8 M5 2 V8" stroke="var(--maroon)" stroke-width=".6"/></svg>
        www.coralbendpastoral.com
      </li>
    </ul>
  </section>
</main>
</body>
</html>
```